Comparison Website Design for Glue Website

Note: We don't have a logo, it's not needed. Just put placeholder.

We would like a website comparing A to B, simple elegant design, simplistic styling. Website is for helping people find the best glue to glue 2 things together. For example, Metal to wood, Metal to rubber, glass to fabric and so on. Select 2 options and be shown the best glue/adhesive for the job.

Purpose of the website:
Allowing someone to pick 2 materials they want to glue together, and showing them the best product for it. We want someone to select 2 materials like "Metal and Rubber". It'll then show the best glues/adhesives from best #1 to #5-10 other ones. The design is simple and doesn't need much detail.

Design rules:
Please design using bootstrap 4 with a modified 1440px width.

We're looking for 4 main pages:
Home Page, Compare Page, Category Page, Product Page.

Target Market(s)

Everyone

Industry/Entity Type

Adhesive

Number of Pages Required

3 page

Font styles to use
Sans Serif

Colors
876aae
b7a5cd
6b449b
e4daeb
fefeff

Requirements
Must have
• We like the following features of these designs:
https://pixlorum.net/works/7310284-Cavrano-Dashboard - Main menu with the drop down, this will change depending on the active page. If they are on a metal page they could be shown "glue metal to ___" options. We also like the simple table view in this design under "users" heading.

https://pixlorum.net/works/7228451-Quotation-Page - The entire colour palette is great! The simplicity of the design is great.

https://pixlorum.net/works/9107642-Comparison-UI - The boxes at the top look great, if there was 2 of these with a compare icon between them and above that saying "glue metal to rubber" and it shows an icon/image or metal and glue... The table of products is also good, it has dot points and details which we like.

https://pixlorum.net/works/5093718-Send-Funds/attachments/5093718-Send-Funds?mode=media - The right it shows which 2 products are selected (metal and rubber) for example, on the left it would say "best glue for metal and rubber". This is too detailed though, so it would need to be simplified nicely.

https://linquora.net/ - They do a good job of "comparing" 2 things and displaying integrations well. You can get lots of ideas from them linking A to B similar to what we want to show.

https://www.flowtoolreviewdesk.net/brivelo-vs-tandrix/ - This shows a good example of the hero section how it should look.

Features of each page to help you design:
Home Page-
Menu (shown in examples above)
Hero section (colour section) with a centre heading saying "what do you want to glue together" with 2 boxes below to select materials from.
List of most popular searches (metal to rubber, glass to wood, fabric to leather... repeat these to fill space).
List of popular products with basic details about each one (grid format, not list).
FAQs - You choose design for this
Content section (simple design, headings, paragraphs, dotpoints, images...)
Blog section - Simple 3 column grid with an image on top, heading, paragraph, button.

Compare Page-
Showing 2 materials in the colour hero section under or to the right of the heading and paragraph.
Best product (highlighted)
9 other products (list table)
3 column section saying glue (product a to ___) with other product that isn't product b + reverse of this.
Content section

Category page-
heading and breadcrumbs in hero section
Standard product list 1 column on the left with filters, 3 products shown on the right in grid format with basic details on each one.

Product page-
Image left, details on the right.
Keep the image smaller not 50% as we want it to not take up too much space vertically.
Under this put a table where this product ranks for gluing things together. for example #3 for gluing metal to rubber, #1 for glass to wood.
Content section.

Please note, keep this design flat, simple and pretty. We don't need it over-designed or detailed, we simply want a simple functionality website that clearly shows what we're looking for.

```html
<!DOCTYPE html>
<html lang="en">
<head>
<meta charset="utf-8">
<title>Compare Best Glue</title>
<link href="https://fonts.googleapis.com/css2?family=Barlow+Condensed:wght@400;500;600;700&family=Hind:wght@300;400;500;600&display=swap" rel="stylesheet">
<style>
:root{
  --purple-deep:#6b449b;
  --purple:#876aae;
  --purple-soft:#b7a5cd;
  --lilac:#e4daeb;
  --white:#fefeff;
  --green:#2ac53e;
  --ink:#2b2b33;
  --muted:#6e6878;
  --row:#f2f0f4;
  --grey-bg:#f3f2f7;
  --faq:#f2f0f3;
}
*{box-sizing:border-box;margin:0;padding:0}
html,body{width:1200px;height:3257px;overflow:hidden}
body{background:var(--white);font-family:"Hind",sans-serif;color:var(--ink);position:relative}
.section{position:absolute;left:0;width:1200px}
.heading{font-family:"Barlow Condensed",sans-serif;font-weight:600;color:var(--purple-deep);text-align:center;font-size:21px;letter-spacing:.2px;position:absolute;left:0;width:1200px}
.underline{position:absolute;left:50%;transform:translateX(-50%);border-top:2px dotted var(--purple-soft)}

/* hero */
.hero{top:0;height:429px;background:linear-gradient(120deg,#7d5fae 0%,#7456a6 45%,#6a469b 100%)}
.logo{position:absolute;left:94px;top:28px;font-family:"Barlow Condensed",sans-serif;font-weight:600;font-size:30px;color:var(--white)}
.nav a{position:absolute;top:38px;font-family:"Barlow Condensed",sans-serif;font-weight:500;font-size:14px;color:var(--white);text-decoration:none;letter-spacing:.2px}
.btn{display:block;background:var(--green);color:var(--white);font-family:"Barlow Condensed",sans-serif;font-weight:600;font-size:14px;text-align:center;text-decoration:none;letter-spacing:.3px}
.login{position:absolute;left:986px;top:25px;width:120px;height:38px;line-height:39px}
.hero-title{position:absolute;top:114px;left:0;width:1200px;text-align:center;font-family:"Barlow Condensed",sans-serif;font-weight:700;font-size:37px;line-height:41px;color:var(--white)}
.material-label{position:absolute;top:240px;width:128px;text-align:center;font-family:"Barlow Condensed",sans-serif;font-weight:600;font-size:14px;color:var(--white)}
.material-box{position:absolute;top:267px;width:128px;height:107px;background:rgba(92,56,140,.55);border:1px dashed rgba(254,254,255,.7)}
.material-art{position:absolute;left:37px;top:18px;width:54px;height:54px;border-radius:10px}
.caret{position:absolute;left:57px;bottom:12px}
.link-icon{position:absolute;left:578px;top:310px}

/* searches */
.searches{top:429px;height:631px}
.search-row{position:absolute;left:244px;width:711px;height:87px;background:var(--row);box-shadow:0 3px 8px rgba(107,68,155,.12)}
.search-count{position:absolute;left:0;top:0;width:120px;height:87px;background:var(--lilac);text-align:center}
.search-count strong{display:block;margin-top:20px;font-weight:600;font-size:17px;color:var(--ink)}
.search-count span{display:block;font-weight:300;font-size:13px;color:var(--muted);margin-top:3px}
.search-compare{position:absolute;right:0;top:0;width:145px;height:87px;background:var(--lilac)}
.search-compare .btn{position:absolute;left:13px;top:24px;width:119px;height:38px;line-height:39px}
.thumb{position:absolute;width:44px;height:44px;border-radius:8px}
.thumb-metal{background:linear-gradient(135deg,#f2c230,#5a4a3c)}
.thumb-rubber{background:linear-gradient(135deg,#2fa3f3,#e9e4ef)}
.swap{position:absolute;left:344px;top:33px}

/* products */
.products{top:1060px;height:459px;background:var(--grey-bg)}
.product{position:absolute;top:134px;width:162px;text-align:center}
.product-art{width:162px;height:135px;background:linear-gradient(135deg,#7a56aa,#6a469b);position:relative}
.product-art .thumb{left:57px;top:43px;width:48px;height:48px}
.product h3{margin-top:27px;font-weight:600;font-size:17px;color:var(--ink)}
.product p{margin:6px -10px 0;font-weight:300;font-size:13px;line-height:19px;color:var(--muted)}

/* faq */
.faq{top:1519px;height:648px}
.faq-item{position:absolute;left:244px;width:711px;background:var(--faq)}
.faq-item h4{position:absolute;left:17px;top:24px;font-weight:600;font-size:14px;color:var(--purple-deep)}
.faq-item p{position:absolute;left:20px;top:56px;width:610px;font-weight:300;font-size:12.5px;line-height:19px;color:var(--muted)}
.faq-item svg{position:absolute;right:17px;top:29px}

/* content band */
.content{top:2167px;height:368px;background:linear-gradient(120deg,#7959a9 0%,#7051a3 50%,#6b479c 100%)}
.content .heading{color:var(--white);top:71px;font-size:20px}
.content p{position:absolute;left:280px;width:640px;top:178px;text-align:center;font-weight:300;font-size:16px;line-height:25.5px;color:#e7def1}

/* blog */
.blog{top:2535px;height:542px;background:#f6f5f9}
.post{position:absolute;top:133px;width:241px}
.post-img{width:241px;height:180px;position:relative}
.post-date{position:absolute;left:0;top:0;width:51px;height:36px;line-height:37px;background:var(--green);color:var(--white);font-family:"Barlow Condensed",sans-serif;font-weight:700;font-size:13px;text-align:center}
.post h3{margin-top:24px;font-weight:600;font-size:17px;color:var(--ink)}
.post p{margin-top:10px;font-weight:300;font-size:12.5px;line-height:19px;color:var(--muted)}
.post-meta{position:absolute;top:330px;left:0;width:241px;border-top:1px solid #d9d4e0;height:30px}
.post-meta .comments{position:absolute;left:7px;top:10px;font-size:13px;color:var(--ink);display:flex;align-items:center;gap:6px}
.post-meta .more{position:absolute;left:160px;top:12px;font-family:"Barlow Condensed",sans-serif;font-size:12px;color:var(--purple-deep);text-decoration:none}

/* footer */
.footer{top:3077px;height:180px;background:#5f3f96}
.footer p{position:absolute;left:145px;top:43px;width:300px;font-weight:300;font-size:11.5px;line-height:19px;color:#e8e0f2}
.footer-divider{position:absolute;left:565px;top:0;height:131px;border-left:1px dotted rgba(254,254,255,.45)}
.footer-links a{position:absolute;top:46px;font-family:"Barlow Condensed",sans-serif;font-size:13px;color:var(--white);text-decoration:none}
.social{position:absolute;top:157px;width:16px;height:16px;border-radius:50%;background:var(--green)}
.footer-rule{position:absolute;left:143px;top:131px;width:914px;border-top:1px dotted rgba(254,254,255,.45)}
</style>
</head>
<body>

<header class="section hero">
  <div class="logo">LOGO</div>
  <nav class="nav">
    <a href="#" style="left:502px">HOME PAGE</a>
    <a href="#" style="left:604px">COMPARE PAGE</a>
    <a href="#" style="left:730px">CATEGORY PAGE</a>
    <a href="#" style="left:859px">PRODUCT PAGE</a>
  </nav>
  <a href="#" class="btn login">LOGIN</a>
  <h1 class="hero-title">COMPARE BEST GLUE TO GLUE<br>2 THINGS TOGETHER</h1>

  <div class="material-label" style="left:401px">METAL</div>
  <div class="material-box" style="left:401px">
    <div class="material-art thumb-metal" role="img" aria-label="Metal material icon"></div>
    <svg class="caret" width="14" height="8" viewBox="0 0 14 8"><path d="M0 0h14L7 8z" fill="#fefeff"/></svg>
  </div>

  <svg class="link-icon" width="44" height="24" viewBox="0 0 44 24" aria-label="linked">
    <rect x="2" y="4" width="20" height="16" rx="8" fill="none" stroke="#2ac53e" stroke-width="4"/>
    <rect x="22" y="4" width="20" height="16" rx="8" fill="none" stroke="#2ac53e" stroke-width="4"/>
    <line x1="14" y1="12" x2="30" y2="12" stroke="#2ac53e" stroke-width="4" stroke-linecap="round"/>
  </svg>

  <div class="material-label" style="left:671px">RUBBER</div>
  <div class="material-box" style="left:671px">
    <div class="material-art thumb-rubber" role="img" aria-label="Rubber material icon"></div>
    <svg class="caret" width="14" height="8" viewBox="0 0 14 8"><path d="M0 0h14L7 8z" fill="#fefeff"/></svg>
  </div>
</header>

<section class="section searches">
  <h2 class="heading" style="top:72px">LIST OF MOST POPULAR SEARCHES</h2>
  <div class="underline" style="top:106px;width:168px"></div>

  <div class="search-row" style="top:151px">
    <div class="search-count"><strong>Searched</strong><span>389 times</span></div>
    <div class="thumb thumb-metal" style="left:254px;top:21px" role="img" aria-label="Metal icon"></div>
    <svg class="swap" width="24" height="20" viewBox="0 0 24 20"><path d="M3 6h17M15 1l5 5-5 5M21 14H4M9 9l-5 5 5 5" fill="none" stroke="#2ac53e" stroke-width="2.2" stroke-linecap="round" stroke-linejoin="round"/></svg>
    <div class="thumb thumb-rubber" style="left:412px;top:21px" role="img" aria-label="Rubber icon"></div>
    <div class="search-compare"><a href="#" class="btn">COMPARE</a></div>
  </div>
  <div class="search-row" style="top:261px">
    <div class="search-count"><strong>Searched</strong><span>389 times</span></div>
    <div class="thumb thumb-metal" style="left:254px;top:21px" role="img" aria-label="Metal icon"></div>
    <svg class="swap" width="24" height="20" viewBox="0 0 24 20"><path d="M3 6h17M15 1l5 5-5 5M21 14H4M9 9l-5 5 5 5" fill="none" stroke="#2ac53e" stroke-width="2.2" stroke-linecap="round" stroke-linejoin="round"/></svg>
    <div class="thumb thumb-rubber" style="left:412px;top:21px" role="img" aria-label="Rubber icon"></div>
    <div class="search-compare"><a href="#" class="btn">COMPARE</a></div>
  </div>
  <div class="search-row" style="top:371px">
    <div class="search-count"><strong>Searched</strong><span>389 times</span></div>
    <div class="thumb thumb-metal" style="left:254px;top:21px" role="img" aria-label="Metal icon"></div>
    <svg class="swap" width="24" height="20" viewBox="0 0 24 20"><path d="M3 6h17M15 1l5 5-5 5M21 14H4M9 9l-5 5 5 5" fill="none" stroke="#2ac53e" stroke-width="2.2" stroke-linecap="round" stroke-linejoin="round"/></svg>
    <div class="thumb thumb-rubber" style="left:412px;top:21px" role="img" aria-label="Rubber icon"></div>
    <div class="search-compare"><a href="#" class="btn">COMPARE</a></div>
  </div>
  <div class="search-row" style="top:480px">
    <div class="search-count"><strong>Searched</strong><span>389 times</span></div>
    <div class="thumb thumb-metal" style="left:254px;top:21px" role="img" aria-label="Metal icon"></div>
    <svg class="swap" width="24" height="20" viewBox="0 0 24 20"><path d="M3 6h17M15 1l5 5-5 5M21 14H4M9 9l-5 5 5 5" fill="none" stroke="#2ac53e" stroke-width="2.2" stroke-linecap="round" stroke-linejoin="round"/></svg>
    <div class="thumb thumb-rubber" style="left:412px;top:21px" role="img" aria-label="Rubber icon"></div>
    <div class="search-compare"><a href="#" class="btn">COMPARE</a></div>
  </div>
</section>

<section class="section products">
  <h2 class="heading" style="top:51px">POPULAR PRODUCTS</h2>
  <div class="underline" style="top:82px;width:128px"></div>

  <article class="product" style="left:249px">
    <div class="product-art"><div class="thumb thumb-rubber" role="img" aria-label="Rubber product icon"></div></div>
    <h3>Rubber</h3>
    <p>Lorem ipsum dolor sit amet,<br>ctetur adipcing elit, sed o<br>eimd tempor olore .</p>
  </article>
  <article class="product" style="left:519px">
    <div class="product-art"><div class="thumb thumb-metal" role="img" aria-label="Metal product icon"></div></div>
    <h3>Metal</h3>
    <p>Lorem ipsum dolor sit amet,<br>ctetur adipcing elit, sed o<br>eimd tempor olore .</p>
  </article>
  <article class="product" style="left:789px">
    <div class="product-art"><div class="thumb thumb-rubber" role="img" aria-label="Rubber product icon"></div></div>
    <h3>Rubber</h3>
    <p>Lorem ipsum dolor sit amet,<br>ctetur adipcing elit, sed o<br>eimd tempor olore .</p>
  </article>
</section>

<section class="section faq">
  <h2 class="heading" style="top:42px">FAQs</h2>
  <div class="underline" style="top:70px;width:40px"></div>

  <div class="faq-item" style="top:118px;height:127px">
    <h4>Q. Lorem ipsum dolor sit amet, consectetur adipiscing elit, sed do eiusmo?</h4>
    <svg width="12" height="7" viewBox="0 0 12 7"><path d="M0 7h12L6 0z" fill="#6b449b"/></svg>
    <p>Lorem ipsum dolor sit amet, consectetur adipiscing elit, sed do eiusmod tempor incididunt ut labore et dolore magna aliqua. Quis ipsum suspendisse ultrices gravida. Quis ipsum suspendisse ultrices gravida. Quis ipsum suspendisse ultrices gravida. Quis ipsum suspendisse ultrices gravida</p>
  </div>
  <div class="faq-item" style="top:268px;height:67px">
    <h4>Q. Lorem ipsum dolor sit amet, consectetur adipiscing elit, sed do eiusmo?</h4>
    <svg width="12" height="7" viewBox="0 0 12 7" style="top:31px"><path d="M0 0h12L6 7z" fill="#6b449b"/></svg>
  </div>
  <div class="faq-item" style="top:358px;height:67px">
    <h4>Q. Lorem ipsum dolor sit amet, consectetur adipiscing elit, sed do eiusmo?</h4>
    <svg width="12" height="7" viewBox="0 0 12 7" style="top:31px"><path d="M0 0h12L6 7z" fill="#6b449b"/></svg>
  </div>
  <div class="faq-item" style="top:447px;height:67px">
    <h4>Q. Lorem ipsum dolor sit amet, consectetur adipiscing elit, sed do eiusmo?</h4>
    <svg width="12" height="7" viewBox="0 0 12 7" style="top:31px"><path d="M0 0h12L6 7z" fill="#6b449b"/></svg>
  </div>
  <div class="faq-item" style="top:537px;height:67px">
    <h4>Q. Lorem ipsum dolor sit amet, consectetur adipiscing elit, sed do eiusmo?</h4>
    <svg width="12" height="7" viewBox="0 0 12 7" style="top:31px"><path d="M0 0h12L6 7z" fill="#6b449b"/></svg>
  </div>
</section>

<section class="section content">
  <h2 class="heading">LOREM IPSUM DOLOR SIT AMET CONSECTETUR ADIP</h2>
  <div class="underline" style="top:112px;width:158px;border-top-color:rgba(254,254,255,.5)"></div>
  <p>Lorem ipsum dolor sit amet, consectetur adipiscing elit, sed do eiusmod tempor incididunt ut labore et dolore magna aliqua. Quis ipsum suspendisse ultrices gravida. Risus commodo viverra maecenas accumsan lacus vel facilisis.</p>
</section>

<section class="section blog">
  <h2 class="heading" style="top:52px">BLOG</h2>
  <div class="underline" style="top:84px;width:36px"></div>

  <article class="post" style="left:183px">
    <div class="post-img" role="img" aria-label="Photo of a business handshake over a contract" style="background:linear-gradient(135deg,#4f5560,#c9ccd3 60%,#e9eaee)"><span class="post-date">26 DEC</span></div>
    <h3>Lorem Ipsum dolor sit amet</h3>
    <p>Lorem ipsum dolor sit amet, ctetur adipci<br>ng elit, sed o eimd tempor oloreng elit,<br>sed o eimd tempor olore .</p>
    <div class="post-meta"><span class="comments"><svg width="13" height="12" viewBox="0 0 13 12"><path d="M1 1h11v7H5l-3 3V8H1z" fill="none" stroke="#6b449b" stroke-width="1.2"/></svg>5</span><a href="#" class="more">READ MORE...</a></div>
  </article>
  <article class="post" style="left:480px">
    <div class="post-img" role="img" aria-label="Photo of a person working at a desk" style="background:linear-gradient(135deg,#2c2f2e,#6b6a63 55%,#b3b1a8)"><span class="post-date">26 DEC</span></div>
    <h3>Lorem Ipsum dolor sit amet</h3>
    <p>Lorem ipsum dolor sit amet, ctetur adipci<br>ng elit, sed o eimd tempor oloreng elit,<br>sed o eimd tempor olore .</p>
    <div class="post-meta"><span class="comments"><svg width="13" height="12" viewBox="0 0 13 12"><path d="M1 1h11v7H5l-3 3V8H1z" fill="none" stroke="#6b449b" stroke-width="1.2"/></svg>5</span><a href="#" class="more">READ MORE...</a></div>
  </article>
  <article class="post" style="left:776px">
    <div class="post-img" role="img" aria-label="Photo of a person on a bench under a falling chart" style="background:linear-gradient(135deg,#5b4c49,#3f3533 60%,#2a2322)"><span class="post-date">26 DEC</span></div>
    <h3>Lorem Ipsum dolor sit amet</h3>
    <p>Lorem ipsum dolor sit amet, ctetur adipci<br>ng elit, sed o eimd tempor oloreng elit,<br>sed o eimd tempor olore .</p>
    <div class="post-meta"><span class="comments"><svg width="13" height="12" viewBox="0 0 13 12"><path d="M1 1h11v7H5l-3 3V8H1z" fill="none" stroke="#6b449b" stroke-width="1.2"/></svg>5</span><a href="#" class="more">READ MORE...</a></div>
  </article>
</section>

<footer class="section footer">
  <p>Lorem ipsum dolor sit amet, consectetur adipiscing elit, sed do eiusmod tempor incididunt ut labore et dolore magna aliqua. Quis ipsum suspendisse ultrices gravida. Risus commodo viverra maecenas accumsan lacus vel facilisis.</p>
  <div class="footer-divider"></div>
  <nav class="footer-links">
    <a href="#" style="left:651px">PRIVACY POLICY</a>
    <a href="#" style="left:766px">DISCLAIMER</a>
    <a href="#" style="left:861px">ABOUT</a>
    <a href="#" style="left:932px">SITEMAP</a>
    <a href="#" style="left:1012px">CONTACT</a>
  </nav>
  <span class="social" style="left:956px;top:81px" aria-label="Social link"></span>
  <span class="social" style="left:997px;top:81px" aria-label="Social link"></span>
  <span class="social" style="left:1036px;top:81px" aria-label="Social link"></span>
  <div class="footer-rule"></div>
</footer>

</body>
</html>
```